Under 16 Cricket Tour To Malaysia

I need a flyer to promote an under 16 cricket to Malaysia
The tour will run from April 25th 2108 to May the 7th

Target Market(s)

Boys aged 15-16

Industry/Entity Type

Tour

Font styles to use
Serif

Colors
0255a3
ec1f27

Requirements
Must have
• Dates of the tour
• T20 and Limited Overs games against teams from 5 other countries.
• Name of the tournament is Pelangi Invitational Under 16 Cricket Tournament
• Level 3 coaches with international experience
• Contact Marcus at marcus@brightwickathletics.com.au for more information.

```html
<!DOCTYPE html>
<html lang="en">
<head>
<meta charset="utf-8">
<title>Pelangi Invitational Under 16 Cricket Tournament – Flyer</title>
<link rel="stylesheet" href="https://fonts.googleapis.com/css2?family=Archivo+Black&family=Oswald:wght@500&family=Open+Sans:wght@400;700&display=swap">
<style>
  :root {
    --blue: #0255a3;
    --red: #ec1f27;
    --orange: #e8801c;
    --purple: #7b3f98;
    --ink: #1d1d1f;
    --paper: #ffffff;
    --backdrop: #ece8e1;
    --wash-warm: #f1b63c;
    --wash-cool: #5a8fd6;
  }
  html, body {
    margin: 0;
    width: 1200px;
    height: 1200px;
    overflow: hidden;
    background: var(--backdrop);
  }
  .flyer {
    position: absolute;
    left: 190px;
    top: 20px;
    width: 820px;
    height: 1160px;
    background: var(--paper);
    box-shadow: 0 6px 24px rgba(0,0,0,0.18);
  }
  .flyer svg { display: block; width: 100%; height: 100%; }
  .display { font-family: "Archivo Black", sans-serif; }
  .condensed { font-family: "Oswald", sans-serif; font-weight: 500; }
  .body-text { font-family: "Open Sans", sans-serif; }
  .fill-blue { fill: var(--blue); }
  .fill-red { fill: var(--red); }
  .fill-orange { fill: var(--orange); }
  .fill-purple { fill: var(--purple); }
  .fill-ink { fill: var(--ink); }
  .fill-white { fill: var(--paper); }
</style>
</head>
<body>
<main class="flyer">
  <svg viewBox="0 0 958 1355" xmlns="http://www.w3.org/2000/svg">
    <defs>
      <radialGradient id="action-wash" cx="50%" cy="50%" r="60%">
        <stop offset="0%" stop-color="var(--wash-cool)"/>
        <stop offset="55%" stop-color="var(--wash-warm)"/>
        <stop offset="100%" stop-color="#f6d68a"/>
      </radialGradient>
    </defs>

    <!-- diagonal stripes -->
    <polygon class="stripe-red fill-red" points="0,760 958,316 958,426 0,892"/>
    <polygon class="stripe-blue fill-blue" points="0,990 958,556 958,690 0,1124"/>

    <!-- organiser name -->
    <g class="organiser">
      <circle cx="150" cy="74" r="34" fill="none" stroke="var(--red)" stroke-width="7"/>
      <text x="150" y="143" text-anchor="middle" class="display fill-blue" font-size="17" letter-spacing="1">BRIGHTWICK ATHLETICS</text>
    </g>

    <!-- tournament title -->
    <g class="title display">
      <text class="fill-red" font-size="60" transform="translate(23,351) rotate(-25)" textLength="690" lengthAdjust="spacingAndGlyphs">PELANGI INVITATIONAL</text>
      <text class="fill-blue" font-size="100" transform="translate(73,430) rotate(-25)" textLength="880" lengthAdjust="spacingAndGlyphs">UNDER 16 CRICKET</text>
      <text class="fill-orange" font-size="150" transform="translate(43,580) rotate(-25)" textLength="930" lengthAdjust="spacingAndGlyphs">TOURNAMENT</text>
      <text class="fill-purple" font-size="82" transform="translate(568,456) rotate(-25)" textLength="340" lengthAdjust="spacingAndGlyphs">MALAYSIA</text>
    </g>

    <!-- cricket action artwork area -->
    <g role="img" aria-label="Illustration of young cricketers in action: a batsman mid-stroke, a bowler, fielders diving and a wicketkeeper, on a painted orange splash">
      <ellipse cx="470" cy="770" rx="300" ry="310" fill="url(#action-wash)" opacity="0.9"/>
    </g>

    <!-- dates -->
    <g class="dates display">
      <polygon class="fill-red" points="383,1028 808,1028 838,1091 413,1091"/>
      <text x="476" y="1078" class="fill-white" font-size="42">April</text>
      <text x="632" y="1080" class="fill-white" font-size="52">25<tspan font-size="28" dy="-26">th</tspan></text>
      <polygon class="fill-blue" points="468,1094 908,1094 938,1171 498,1171" />
      <text x="530" y="1145" class="fill-white" font-size="26">TO</text>
      <text x="590" y="1148" class="fill-white" font-size="48">May</text>
      <text x="728" y="1152" class="fill-white" font-size="52">7<tspan font-size="28" dy="-26">th</tspan></text>
      <text x="713" y="1233" text-anchor="middle" class="fill-ink" font-size="60" letter-spacing="2">2018</text>
    </g>

    <!-- partner name -->
    <g class="partner">
      <text x="225" y="1168" text-anchor="middle" class="display fill-red" font-size="32">HARBOURLINE SPORTS</text>
      <text x="225" y="1208" text-anchor="middle" class="condensed fill-ink" font-size="26" letter-spacing="1">SEAFORD</text>
    </g>

    <!-- footer -->
    <g class="footer">
      <polygon class="fill-blue" points="0,1262 303,1262 338,1355 0,1355"/>
      <polygon class="fill-red" points="318,1262 958,1262 958,1355 358,1355"/>
      <text x="20" y="1297" class="body-text fill-white" font-size="14">For More Information Contact <tspan font-weight="700" font-size="24">Marcus</tspan></text>
      <line x1="20" y1="1304" x2="300" y2="1304" stroke="var(--paper)" stroke-width="1.5"/>
      <text x="20" y="1330" class="body-text fill-white" font-size="14.5" textLength="285" lengthAdjust="spacingAndGlyphs">marcus@<tspan font-weight="700">brightwickathletics</tspan>.com.au</text>
      <text x="942" y="1299" text-anchor="end" class="condensed fill-white" font-size="21">T20 and Limited Overs games against teams from 5 other countries.</text>
      <text x="942" y="1328" text-anchor="end" class="condensed fill-white" font-size="21">Level 3 coaches with international experience</text>
    </g>
  </svg>
</main>
</body>
</html>
```